Freelance yoga teacher looking for professional postcard design

I need a postcard that shows my class times & venues. I also would like it to show that I offer private one to one sessions for those not ready for group practice, or who require personal attention. It needs to show my contact details - mob: 07346218850, email & website addresses. I also want the opportunity to add other services in future, such as my website and yoga massage.

UPDATE 18 JULY

FRONT OF POSTCARD
I would like the front side of the postcard to not look too busy or 'wordy'. If using bullet points, be creative, so no ticks. Please use my full name Maren T Holloway NCM Dip.

REVERSE SIDE
The reverse side I think should have the NCM logo, together with words describing classes, 'classes are designed...' please omit the sentences starting 'by running courses...'

'Postage required' or lines for an address are not required.

Make the 'where I teach' venues/times look personable, so no harsh gridlines please.

Target Market(s)

Most of my students are 30+ professionals with disposable income or early retirees.

Industry/Entity Type

Teacher

Requirements
Must have
• It must show my National Circle of Movement Teacher Logo which I can supply.
Maren T Holloway is a National Circle of Movement trained teacher.
Classes are small and friendly, designed to create ease in the body, reduce stress and promote relaxation. Maren is passionate about sharing yoga, respecting each individual and modifying to suit their needs, leading to improved function, mobility and stability.

Keep any images simple, such as rolled up yoga mats. I am commissioning a personal mandala which I will use as a logo, but this will not be ready until mid to late August.

Please see attached 'attempt' at a postcard giving details of classes/venues, contact info.
Nice to have
• Somewhere on the postcard the words: 'Yoga. Centre the body & mind. Stretch the possibilities.'
Should not have
• Images of people doing yoga or silhouettes of yoga postures.

```html
<!DOCTYPE html>
<html lang="en">
<head>
<meta charset="UTF-8">
<title>Yoga with Maren T Holloway – Postcard</title>
<link rel="stylesheet" href="https://fonts.googleapis.com/css2?family=Tinos:wght@400;700&display=swap">
<style>
  :root {
    --orange: #f56a0b;
    --orange-deep: #d95a05;
    --black: #000000;
    --white: #ffffff;
    --ink: #111111;
    --logo-blue: #3f6ea3;
  }
  * { box-sizing: border-box; margin: 0; padding: 0; }
  html, body {
    width: 1200px; height: 462px; overflow: hidden;
    background: var(--black);
    font-family: "Tinos", "Times New Roman", serif;
  }
  .canvas { position: relative; width: 1200px; height: 462px; background: var(--black); }

  /* Corner flourishes */
  .corner-ornament {
    position: absolute; width: 58px; height: 54px;
    background: linear-gradient(135deg, var(--orange) 0%, var(--orange-deep) 45%, var(--black) 100%);
    border-radius: 4px;
  }

  /* Front card */
  .front {
    position: absolute; left: 0; top: 0; width: 598px; height: 462px;
    background: var(--black); border: 3px solid var(--black);
  }
  .front__header {
    position: absolute; left: 0; top: 0; width: 592px; height: 115px;
    background: var(--white);
  }
  .front .corner-ornament--tl { left: 8px; top: 8px; }
  .front .corner-ornament--tr { right: 8px; top: 8px; transform: scaleX(-1); }
  .front__name {
    position: absolute; left: 0; right: 0; top: 52px;
    text-align: center; font-weight: 700; font-size: 29px; line-height: 32px;
    color: var(--ink); letter-spacing: 0.3px;
  }
  .front__qualification { font-size: 19px; letter-spacing: 0.5px; }

  .front__details {
    position: absolute; left: 0; top: 115px; width: 592px; height: 258px;
    background: var(--orange); color: var(--white);
  }
  .detail {
    position: absolute; left: 64px; display: flex; align-items: flex-end;
    font-size: 17px; line-height: 1;
  }
  .detail__bullet {
    width: 14px; height: 14px; border-radius: 50%;
    background: var(--white); margin-right: 26px; margin-bottom: 1px;
  }
  .detail__label { white-space: nowrap; }
  .detail__line {
    display: inline-block; border-bottom: 1px solid var(--white);
    margin-left: 6px; height: 1px; margin-bottom: 1px;
  }
  .detail--times   { top: 40px; }
  .detail--venues  { top: 82px; }
  .detail--mobile  { top: 122px; }
  .detail--email   { top: 158px; }
  .detail--website { top: 201px; }

  .front__figure {
    position: absolute; left: 484px; top: 112px; width: 96px; height: 138px;
    background: var(--white);
    border-radius: 48px 48px 30px 30px;
  }

  .front__footer {
    position: absolute; left: 0; top: 373px; width: 592px; height: 83px;
    background: var(--black); color: var(--white);
    font-weight: 700; font-size: 16px; line-height: 19px;
    text-align: center; padding-top: 24px;
  }

  /* Reverse card */
  .reverse {
    position: absolute; left: 612px; top: 32px; width: 580px; height: 406px;
    background: var(--white); border: 2px solid var(--black);
  }
  .reverse .corner-ornament { width: 62px; height: 58px; }
  .reverse .corner-ornament--tl { left: 2px; top: 2px; }
  .reverse .corner-ornament--tr { right: 2px; top: 2px; transform: scaleX(-1); }
  .reverse .corner-ornament--bl { left: 2px; bottom: 2px; transform: scaleY(-1); }
  .reverse .corner-ornament--br { right: 2px; bottom: 2px; transform: scale(-1,-1); }

  .reverse__title {
    position: absolute; left: 0; right: 0; top: 35px;
    text-align: center; font-weight: 700; font-size: 25px; color: var(--ink);
  }
  .reverse__intro {
    position: absolute; left: 8px; width: 565px; top: 76px;
    font-size: 16.5px; line-height: 22.5px; color: var(--ink); white-space: nowrap;
  }

  .teacher-mark {
    position: absolute; left: 190px; top: 186px; width: 200px; height: 208px;
    display: flex; flex-direction: column; align-items: center; justify-content: center;
    gap: 14px; text-align: center;
  }
  .teacher-mark__circle {
    width: 120px; height: 120px; border-radius: 50%;
    border: 3px solid var(--logo-blue); background: var(--white);
  }
  .teacher-mark__name {
    font-size: 15px; line-height: 18px; color: var(--logo-blue); font-weight: 400;
  }
</style>
</head>
<body>
<div class="canvas">

  <section class="front" aria-label="Postcard front">
    <header class="front__header">
      <div class="corner-ornament corner-ornament--tl" role="img" aria-label="Orange and black flourish corner ornament"></div>
      <div class="corner-ornament corner-ornament--tr" role="img" aria-label="Orange and black flourish corner ornament"></div>
      <h1 class="front__name">MAREN T HOLLOWAY <span class="front__qualification">NCM Dip</span></h1>
    </header>

    <div class="front__details">
      <div class="detail detail--times"><span class="detail__bullet"></span><span class="detail__label">Class Times :</span><span class="detail__line" style="width:260px"></span></div>
      <div class="detail detail--venues"><span class="detail__bullet"></span><span class="detail__label">Venues Time :</span><span class="detail__line" style="width:250px"></span></div>
      <div class="detail detail--mobile"><span class="detail__bullet"></span><span class="detail__label">Mobile No. : 07346218850</span></div>
      <div class="detail detail--email"><span class="detail__bullet"></span><span class="detail__label">Email Address :</span><span class="detail__line" style="width:238px"></span></div>
      <div class="detail detail--website"><span class="detail__bullet"></span><span class="detail__label">Website Address :</span><span class="detail__line" style="width:218px"></span></div>
      <div class="front__figure" role="img" aria-label="White seated meditation illustration"></div>
    </div>

    <footer class="front__footer">
      <p>I offer private one to one sessions for those not ready for group practice,<br>or who require personal attention.</p>
    </footer>
  </section>

  <section class="reverse" aria-label="Postcard reverse">
    <div class="corner-ornament corner-ornament--tl" role="img" aria-label="Orange and black flourish corner ornament"></div>
    <div class="corner-ornament corner-ornament--tr" role="img" aria-label="Orange and black flourish corner ornament"></div>
    <div class="corner-ornament corner-ornament--bl" role="img" aria-label="Orange and black flourish corner ornament"></div>
    <div class="corner-ornament corner-ornament--br" role="img" aria-label="Orange and black flourish corner ornament"></div>

    <h2 class="reverse__title">Yoga with Maren T Holloway</h2>
    <p class="reverse__intro">Classes are small and friendly, designed to create ease in the body,<br>reduce stress and promote relaxation.&nbsp; Maren is passionate about sharing<br>yoga, respecting each individual and modifying to suit their needs,<br>leading to improved function, mobility and stability.</p>

    <div class="teacher-mark">
      <span class="teacher-mark__circle"></span>
      <span class="teacher-mark__name">National Circle of Movement<br>Teacher</span>
    </div>
  </section>

</div>
</body>
</html>
```